Harbor Builders PowerPoint Presentation

We need a sales pitch in powerpoint form for a "commercial only" construction company based out of Dallas, TX. We perform commercial only construction including ground up, build to suit, white box and many others. We would like the design to match the color scheme and outlook of the website and brochure that will be attached. Also, attached you will find the old presentation we used (it's terrible). http://www.harborbgx.example/

Target Market(s)

Commercial property managers, commercial building owners, business owners, facility managers, commercial construction managers, construction design teams

Industry/Entity Type

Construction

Requirements
Must have
• Commercial construction pictures. Company overview. Specific industries served.
Should not have
• Residential pictures. Poor quality pictures. Anything that doesn't look like the website or attached brochure.

```html
<!DOCTYPE html>
<html lang="en">
<head>
<meta charset="utf-8">
<title>Harbor Builders — Pitch Deck Overview</title>
<link href="https://fonts.googleapis.com/css2?family=Montserrat:wght@400;700;800&family=Open+Sans:wght@400;600&display=swap" rel="stylesheet">
<style>
:root{
  --orange:#cf7424;
  --orange-soft:#e7a56a;
  --amber:#eaa400;
  --ink:#3b3b3b;
  --grey:#9b9b9b;
  --line:#dcdcdc;
  --pale:#eef0f1;
  --paper:#ffffff;
}
*{box-sizing:border-box}
html,body{margin:0;width:1200px;height:3180px;overflow:hidden;background:var(--paper)}
.deck{display:grid;grid-template-columns:repeat(3,356px);grid-auto-rows:200px;column-gap:30px;row-gap:38px;padding:32px 0 0 38px}
.slide{position:relative;width:356px;height:200px;background:var(--paper);box-shadow:0 2px 7px rgba(0,0,0,.28);overflow:hidden}
.slide>*{position:absolute;margin:0}
.h{font:700 7px/1.35 Montserrat,sans-serif;color:var(--orange);text-transform:uppercase;letter-spacing:.3px}
.h.white{color:#fff}
.h.big{font-size:9px}
.tx{font:400 4.6px/1.5 "Open Sans",sans-serif;color:var(--grey)}
.tx.white{color:#eee}
.tx.c{text-align:center}
.label{font:700 4.6px/1.3 Montserrat,sans-serif;color:var(--orange);text-transform:uppercase}
.ph{background:linear-gradient(160deg,#e9e4dc 0%,#b9bfc6 40%,#6f7d8c 75%,#4c5866 100%)}
.ph.crew{background:linear-gradient(170deg,#e08a2e 0%,#d9b08a 22%,#c7b7a6 40%,#4f78ab 62%,#2f578b 100%)}
.ph.plan{background:linear-gradient(135deg,#f2c21f 0%,#f3d77a 22%,#f4efe6 45%,#dcd8d0 70%,#c9c4bb 100%)}
.ph.dark{background:linear-gradient(135deg,#2f3236 0%,#55595e 45%,#7c7f83 75%,#3e4145 100%)}
.ph.steel{background:linear-gradient(180deg,#b8c3cd 0%,#8d97a2 35%,#3b444e 65%,#1f252c 100%)}
.ph.warm{background:linear-gradient(165deg,#f0a33a 0%,#e7c3a0 30%,#c98f66 55%,#c23d34 80%,#7d2f2a 100%)}
.ph.veil::after{content:"";position:absolute;inset:0;background:rgba(60,60,60,.45)}
.map{background:radial-gradient(ellipse 50% 50% at 50% 50%,#eaa400 0%,#eeb21f 55%,rgba(234,164,0,.55) 75%,rgba(234,164,0,0) 100%)}
.ico{width:14px;height:14px;border:1px solid var(--orange);border-radius:50%}
.ico::after{content:"";position:absolute;left:4px;top:4px;width:4px;height:4px;background:var(--orange);border-radius:1px}
.ico.solid{background:var(--orange)}
.ico.solid::after{background:#fff}
.logo{display:flex;align-items:center;gap:3px;font:800 8px/1 Montserrat,sans-serif;color:var(--ink);letter-spacing:.4px}
.logo::before{content:"";width:8px;height:8px;border-radius:50%;background:var(--orange)}
.logo.light{color:#fff}
.logo.large{font-size:14px;gap:5px}
.logo.large::before{width:13px;height:13px}
.panel{background:var(--orange)}
.social{display:flex;gap:3px}
.social span{width:9px;height:9px;border:1px solid var(--ink);border-radius:50%}
.year{width:20px;height:20px;border:1.5px solid var(--orange);border-radius:50%;background:#fff;font:700 5px/17px Montserrat,sans-serif;color:var(--orange);text-align:center}
.diamond{transform:rotate(45deg)}
</style>
</head>
<body>
<main class="deck">

<!-- row 1 -->
<section class="slide title-slide">
  <h1 class="h big" style="left:0;width:356px;top:70px;text-align:center">Presentation Title</h1>
  <p class="tx c" style="left:0;width:356px;top:86px">Commercial construction partners</p>
  <div class="logo" style="left:146px;top:108px">HARBOR</div>
  <div class="ph plan" role="img" aria-label="Blueprints on a desk" style="left:0;top:182px;width:356px;height:18px"></div>
</section>

<section class="slide title-photo">
  <div class="ph plan" role="img" aria-label="Hard hat resting on blueprints" style="inset:0"></div>
  <div style="left:95px;top:62px;width:166px;height:76px;background:rgba(255,255,255,.88)"></div>
  <h1 class="h big" style="left:95px;width:166px;top:78px;text-align:center">Presentation Title</h1>
  <div class="logo" style="left:150px;top:108px">HARBOR</div>
</section>

<section class="slide title-team">
  <div class="ph crew veil" role="img" aria-label="Two builders in hard hats" style="inset:0"></div>
  <h1 class="h big white" style="left:0;width:356px;top:38px;text-align:center">Lorem Ipsum Dolor</h1>
  <p class="tx white c" style="left:0;width:356px;top:54px">Dallas commercial builders</p>
  <div class="logo light large" style="left:132px;top:140px">HARBOR</div>
</section>

<!-- row 2 -->
<section class="slide brand-mark">
  <div class="ph plan" role="img" aria-label="Hard hat and building plans" style="inset:0"></div>
  <div style="left:60px;top:42px;width:112px;height:112px;border-radius:50%;background:var(--orange)"></div>
</section>

<section class="slide brand-mark-dark">
  <div class="ph dark" role="img" aria-label="Tools laid on a work table" style="inset:0"></div>
  <div style="left:95px;top:42px;width:112px;height:112px;border-radius:50%;background:#f4f1ee"></div>
  <div class="logo light" style="right:14px;top:14px">HARBOR</div>
</section>

<section class="slide intro">
  <div class="ph" role="img" aria-label="Engineer in a helmet on site" style="left:0;top:0;width:210px;height:200px"></div>
  <h2 class="h" style="left:225px;width:118px;top:62px;text-align:right">Neque porro quisquam est qui</h2>
  <p class="tx" style="left:225px;width:118px;top:90px;text-align:right">Build to suit and white box.</p>
  <div class="logo" style="right:12px;top:180px;font-size:6px">HARBOR</div>
</section>

<!-- row 3 -->
<section class="slide what-is">
  <div class="ph crew" role="img" aria-label="Smiling worker giving a thumbs up" style="left:0;top:0;width:130px;height:200px"></div>
  <h2 class="h" style="left:150px;top:14px">What is lorem ipsum?</h2>
  <p class="tx" style="left:150px;top:26px;width:190px">Ground up builds delivered on time and on budget.</p>
  <div class="ico" style="left:150px;top:52px"></div><p class="label" style="left:170px;top:56px">Ground up</p>
  <div class="ico" style="left:150px;top:76px"></div><p class="label" style="left:170px;top:80px">Build suit</p>
  <div class="ico" style="left:150px;top:100px"></div><p class="label" style="left:170px;top:104px">White box</p>
  <div class="ico" style="left:150px;top:124px"></div><p class="label" style="left:170px;top:128px">Tenant finish</p>
  <div class="logo" style="left:150px;top:182px;font-size:6px">HARBOR</div>
</section>

<section class="slide standard">
  <h2 class="h" style="left:12px;top:14px">The standard lorem</h2>
  <p class="tx" style="left:12px;top:26px">Commercial work only</p>
  <div class="ico" style="left:12px;top:70px"></div><p class="label" style="left:12px;top:88px">Retail sites</p>
  <div class="ico" style="left:68px;top:70px"></div><p class="label" style="left:68px;top:88px">Office space</p>
  <div class="ico" style="left:124px;top:70px"></div><p class="label" style="left:124px;top:88px">Medical units</p>
  <div class="ico" style="left:12px;top:120px"></div><p class="label" style="left:12px;top:138px">Warehouses</p>
  <div class="ico" style="left:68px;top:120px"></div><p class="label" style="left:68px;top:138px">Restaurants</p>
  <div class="ico" style="left:124px;top:120px"></div><p class="label" style="left:124px;top:138px">Flex space</p>
  <div class="ph crew" role="img" aria-label="Builders reviewing drawings" style="left:185px;top:0;width:171px;height:200px"></div>
</section>

<section class="slide why">
  <h2 class="h" style="left:40px;top:46px">Why do we use it?</h2>
  <p class="tx" style="left:20px;top:66px;width:100px">Ground up builds delivered on time and on budget.</p>
  <p class="tx" style="left:130px;top:66px;width:100px">White box shells ready for tenant fit out work.</p>
  <div class="logo" style="left:20px;top:182px;font-size:6px">HARBOR</div>
  <div class="ph plan" role="img" aria-label="Rolled construction plans" style="left:245px;top:0;width:111px;height:200px"></div>
</section>

<!-- row 4 -->
<section class="slide since">
  <p class="h big" style="left:12px;top:12px;font-size:13px">1500</p>
  <p class="tx" style="left:12px;top:32px;width:120px">Ground up builds delivered on time and on budget.</p>
  <h2 class="h" style="left:190px;top:14px;width:154px;text-align:right">The standard lorem ipsum passage, used since the 1500s</h2>
  <div class="ph steel" role="img" aria-label="Steel frame building under construction" style="left:0;top:80px;width:356px;height:120px"></div>
  <div class="logo light" style="left:12px;top:184px;font-size:6px">HARBOR</div>
</section>

<section class="slide growth">
  <div class="ph steel" role="img" aria-label="Building frame at dusk" style="left:0;top:0;width:356px;height:80px"></div>
  <h2 class="h" style="left:12px;top:92px;width:130px">Neque porro quisquam est qui dolorem ipsum quia dolor sit amet</h2>
  <p class="h" style="left:170px;top:100px;font-size:11px">▲ +12%</p>
  <p class="tx" style="left:170px;top:118px">Cost savings</p>
  <p class="h" style="left:262px;top:118px;font-size:11px">▼ -10%</p>
  <p class="tx" style="left:262px;top:136px">Schedule delays</p>
  <div class="ph crew" role="img" aria-label="Row of crew photos" style="left:0;top:170px;width:356px;height:30px"></div>
</section>

<section class="slide services">
  <div class="logo" style="right:12px;top:8px;font-size:6px">HARBOR</div>
  <h2 class="h" style="left:12px;top:22px;width:150px">Neque porro quisquam est qui dolorem ipsum quia dolor sit amet</h2>
  <p class="tx" style="left:190px;top:24px;width:150px">Ground up builds delivered on time and on budget.</p>
  <div class="ico" style="left:120px;top:82px"></div><p class="label" style="left:107px;width:40px;top:100px;text-align:center">Site work</p>
  <div class="ico" style="left:160px;top:82px"></div><p class="label" style="left:147px;width:40px;top:100px;text-align:center">Shell build</p>
  <div class="ico" style="left:200px;top:82px"></div><p class="label" style="left:187px;width:40px;top:100px;text-align:center">Fit out</p>
  <div class="ph plan" role="img" aria-label="Plans and tools on a desk" style="left:0;top:120px;width:356px;height:80px"></div>
</section>

<!-- row 5 -->
<section class="slide grid-six">
  <div class="ph crew" role="img" aria-label="Worker in hard hat" style="left:0;top:0;width:118px;height:100px"></div>
  <div class="ico" style="left:171px;top:22px"></div><p class="label" style="left:118px;width:120px;top:42px;text-align:center">Lorem ipsum</p><p class="tx c" style="left:118px;width:120px;top:50px">Retail shell delivery</p>
  <div class="ph" role="img" aria-label="Engineer with helmet" style="left:238px;top:0;width:118px;height:100px"></div>
  <div class="ico" style="left:52px;top:122px"></div><p class="label" style="left:0;width:118px;top:142px;text-align:center">Lorem ipsum</p><p class="tx c" style="left:0;width:118px;top:150px">Office interior upgrades</p>
  <div class="ph plan" role="img" aria-label="Blueprints close up" style="left:118px;top:100px;width:120px;height:100px"></div>
  <div class="ico" style="left:290px;top:122px"></div><p class="label" style="left:238px;width:118px;top:142px;text-align:center">Lorem ipsum</p><p class="tx c" style="left:238px;width:118px;top:150px">Warehouse ground work</p>
</section>

<section class="slide grid-four">
  <div class="ph crew" role="img" aria-label="Two builders with drawings" style="left:0;top:0;width:178px;height:100px"></div>
  <div class="ico" style="left:260px;top:20px"></div><p class="label" style="left:178px;width:178px;top:40px;text-align:center">Lorem ipsum</p><p class="tx c" style="left:178px;width:178px;top:48px">Medical suite builds</p>
  <div class="ico" style="left:82px;top:120px"></div><p class="label" style="left:0;width:178px;top:140px;text-align:center">Lorem ipsum</p><p class="tx c" style="left:0;width:178px;top:148px">Restaurant finish outs</p>
  <div class="ph crew" role="img" aria-label="Worker in blue overalls" style="left:178px;top:100px;width:178px;height:100px"></div>
</section>

<section class="slide two-projects">
  <h2 class="h" style="left:0;width:356px;top:14px;text-align:center">Lorem ipsum dolor sit amet, consectetur adipiscing elit</h2>
  <div class="ph steel" role="img" aria-label="Building at sunset" style="left:30px;top:36px;width:140px;height:76px"></div>
  <div class="ph crew" role="img" aria-label="Worker in blue overalls" style="left:186px;top:36px;width:140px;height:76px"></div>
  <p class="label" style="left:30px;top:120px">Lorem ipsum</p><p class="tx" style="left:30px;top:128px;width:140px">Ground up builds delivered on time and on budget.</p>
  <p class="label" style="left:186px;top:120px">Lorem ipsum</p><p class="tx" style="left:186px;top:128px;width:140px">White box shells ready for tenant fit out work.</p>
</section>

<!-- row 6 -->
<section class="slide three-people">
  <h2 class="h" style="left:0;width:356px;top:14px;text-align:center">Lorem ipsum dolor sit amet, consectetur adipiscing elit</h2>
  <div class="ph crew" role="img" aria-label="Builders reviewing plans" style="left:20px;top:38px;width:100px;height:80px"></div>
  <div class="ph warm" role="img" aria-label="Worker with thumbs up" style="left:128px;top:38px;width:100px;height:80px"></div>
  <div class="ph crew" role="img" aria-label="Worker in blue overalls" style="left:236px;top:38px;width:100px;height:80px"></div>
  <p class="label" style="left:20px;top:126px">Lorem ipsum</p><p class="tx" style="left:20px;top:134px">Project lead team</p>
  <p class="label" style="left:128px;top:126px">Lorem ipsum</p><p class="tx" style="left:128px;top:134px">Site safety crew</p>
  <p class="label" style="left:236px;top:126px">Lorem ipsum</p><p class="tx" style="left:236px;top:134px">Field operations staff</p>
</section>

<section class="slide quote">
  <div class="ph crew" role="img" aria-label="Smiling worker in a warehouse" style="inset:0"></div>
  <div class="panel" style="left:15px;top:0;width:110px;height:200px;opacity:.92"></div>
  <h2 class="h white" style="left:28px;top:26px">Lorem ipsum</h2>
  <p class="h white" style="left:28px;top:42px;font-size:16px">“</p>
  <p class="tx white" style="left:28px;top:62px;width:88px">Ground up builds delivered on time and on budget.</p>
  <div class="ico" style="left:60px;top:112px;border-color:#fff"></div>
  <div class="logo light" style="left:28px;top:176px;font-size:7px">HARBOR</div>
</section>

<section class="slide values">
  <div class="ph dark" role="img" aria-label="Worker in helmet close up" style="inset:0"></div>
  <h2 class="h white" style="left:200px;top:28px;width:140px">Lorem ipsum dolor sit amet, consectetur adipiscing elit, sed do eiusmod</h2>
  <div class="ico solid" style="left:212px;top:92px"></div><p class="tx white c" style="left:199px;width:40px;top:110px">Safe sites</p>
  <div class="ico solid" style="left:252px;top:78px"></div><p class="tx white c" style="left:239px;width:40px;top:96px">Fair bids</p>
  <div class="ico solid" style="left:292px;top:92px"></div><p class="tx white c" style="left:279px;width:40px;top:110px">Fast builds</p>
  <div class="logo light" style="left:12px;top:180px;font-size:7px">HARBOR</div>
</section>

<!-- row 7 -->
<section class="slide collage-why">
  <h2 class="h" style="left:14px;top:40px;width:60px">Why do we use it?</h2>
  <p class="tx" style="left:14px;top:66px;width:70px">Ground up builds delivered on time and on budget.</p>
  <div class="ph crew" role="img" aria-label="Team meeting on site" style="left:90px;top:0;width:130px;height:100px"></div>
  <div class="ph" role="img" aria-label="Worker with helmet" style="left:220px;top:0;width:136px;height:100px"></div>
  <div class="ph warm" role="img" aria-label="Office team discussion" style="left:90px;top:100px;width:90px;height:100px"></div>
  <div class="ph crew" role="img" aria-label="Workers in a hall" style="left:180px;top:100px;width:176px;height:100px"></div>
</section>

<section class="slide collage-panels">
  <div class="panel" style="left:0;top:0;width:178px;height:100px"></div>
  <div class="ico" style="left:82px;top:34px;border-color:#fff"></div><p class="h white" style="left:0;width:178px;top:54px;text-align:center">Lorem ipsum</p>
  <div class="ph crew" role="img" aria-label="Worker in warehouse" style="left:178px;top:0;width:178px;height:100px"></div>
  <div class="ph crew" role="img" aria-label="Builders at a table" style="left:0;top:100px;width:178px;height:100px"></div>
  <div class="panel" style="left:178px;top:100px;width:178px;height:100px"></div>
  <div class="ico" style="left:260px;top:134px;border-color:#fff"></div>
</section>

<section class="slide stacked">
  <h2 class="h" style="left:20px;top:40px">Lorem ipsum<br>dolor sit</h2>
  <p class="tx" style="left:20px;top:62px;width:150px">Ground up builds delivered on time and on budget.</p>
  <div class="ico" style="left:26px;top:120px"></div>
  <div class="ph crew" role="img" aria-label="Builders with drawings" style="left:206px;top:0;width:150px;height:66px"></div>
  <div class="ph crew" role="img" aria-label="Worker in overalls" style="left:206px;top:67px;width:150px;height:66px"></div>
  <div class="ph warm" role="img" aria-label="Two workers outdoors" style="left:206px;top:134px;width:150px;height:66px"></div>
</section>

<!-- row 8 -->
<section class="slide split-rows">
  <div class="ph warm" role="img" aria-label="Two workers in hard hats" style="left:0;top:0;width:100px;height:80px"></div>
  <h2 class="h" style="left:110px;top:14px">Lorem ipsum<br>dolor sit</h2>
  <p class="tx" style="left:220px;top:14px;width:120px">Ground up builds delivered on time and on budget.</p>
  <div class="ico" style="left:60px;top:132px"></div>
  <h2 class="h" style="left:100px;top:126px">Lorem ipsum<br>dolor sit</h2>
  <p class="tx" style="left:100px;top:148px;width:100px">White box shells ready for tenant fit out work.</p>
  <div class="ph crew" role="img" aria-label="Workers in a factory" style="left:210px;top:116px;width:146px;height:84px"></div>
</section>

<section class="slide diamond-feature">
  <h2 class="h" style="left:14px;top:24px;width:90px">The standard lorem ipsum passage, used since the 1500s</h2>
  <p class="tx" style="left:14px;top:70px;width:90px">Ground up builds delivered on time and on budget.</p>
  <div class="ph diamond" role="img" aria-label="Worker in hard hat" style="left:138px;top:44px;width:100px;height:100px"></div>
  <div class="diamond" style="left:110px;top:110px;width:18px;height:18px;border:1px solid var(--orange);background:#fff"></div>
  <div class="diamond" style="left:250px;top:54px;width:18px;height:18px;border:1px solid var(--orange);background:#fff"></div>
</section>

<section class="slide diamond-collage">
  <div class="ph diamond" role="img" aria-label="Plans on a table" style="left:230px;top:-30px;width:70px;height:70px"></div>
  <div class="diamond" style="left:300px;top:-10px;width:60px;height:60px;background:var(--orange-soft)"></div>
  <div class="ph crew diamond" role="img" aria-label="Worker in helmet" style="left:260px;top:50px;width:66px;height:66px"></div>
  <div class="diamond" style="left:210px;top:60px;width:36px;height:36px;background:var(--orange-soft)"></div>
  <div class="ph warm diamond" role="img" aria-label="Worker smiling" style="left:300px;top:112px;width:52px;height:52px"></div>
  <h2 class="h" style="left:14px;top:128px;width:150px">Section 1.10.33 of "de finibus bonorum et malorum", written by Aurelius Ventor in 45 BC</h2>
  <p class="tx" style="left:14px;top:174px;width:150px">White box shells ready for tenant fit out work.</p>
</section>

<!-- row 9 -->
<section class="slide timeline-early">
  <h2 class="h" style="left:0;width:356px;top:14px;text-align:center">Lorem ipsum dolor sit amet, consectetur adipiscing elit</h2>
  <div style="left:20px;top:82px;width:316px;height:1px;background:var(--orange)"></div>
  <div class="year" style="left:51px;top:72px">2011</div><p class="tx c" style="left:31px;width:60px;top:100px">Company founded</p>
  <div class="year" style="left:126px;top:72px">2012</div><p class="tx c" style="left:106px;width:60px;top:100px">First retail</p>
  <div class="year" style="left:195px;top:72px">2013</div><p class="tx c" style="left:175px;width:60px;top:100px">Office wing</p>
  <div class="year" style="left:265px;top:72px">2014</div><p class="tx c" style="left:245px;width:60px;top:100px">Dallas expansion</p>
</section>

<section class="slide timeline-late">
  <h2 class="h" style="left:0;width:356px;top:14px;text-align:center">Lorem ipsum dolor sit amet, consectetur adipiscing elit</h2>
  <div style="left:20px;top:82px;width:316px;height:1px;background:var(--orange)"></div>
  <div class="year" style="left:51px;top:72px">2015</div><p class="tx c" style="left:31px;width:60px;top:100px">Medical suites</p>
  <div class="year" style="left:126px;top:72px">2016</div><p class="tx c" style="left:106px;width:60px;top:100px">Warehouse line</p>
  <div class="year" style="left:195px;top:72px">2017</div><p class="tx c" style="left:175px;width:60px;top:100px">Build suit</p>
  <div class="year" style="left:265px;top:72px">2018</div><p class="tx c" style="left:245px;width:60px;top:100px">New headquarters</p>
</section>

<section class="slide cycle">
  <svg style="left:30px;top:30px" width="140" height="140" viewBox="0 0 140 140" aria-hidden="true">
    <g fill="#e6e8ea" stroke="#fff" stroke-width="3">
      <path d="M70 70 L70 0 A70 70 0 0 1 140 70 Z"/>
      <path d="M70 70 L140 70 A70 70 0 0 1 70 140 Z"/>
      <path d="M70 70 L70 140 A70 70 0 0 1 0 70 Z"/>
      <path d="M70 70 L0 70 A70 70 0 0 1 70 0 Z"/>
    </g>
    <circle cx="70" cy="70" r="26" fill="#fff"/>
    <g fill="none" stroke="#cf7424"><circle cx="100" cy="36" r="6"/><circle cx="104" cy="100" r="6"/><circle cx="36" cy="104" r="6"/><circle cx="36" cy="36" r="6"/></g>
  </svg>
  <p class="label" style="left:80px;top:94px;width:40px;text-align:center">Lorem ipsum</p>
  <h2 class="h" style="left:210px;top:36px">Lorem ipsum<br>dolor sit</h2>
  <p class="tx" style="left:210px;top:58px;width:130px">Ground up builds delivered on time and on budget.</p>
  <p class="tx" style="left:210px;top:84px;width:130px">White box shells ready for tenant fit out work.</p>
</section>

<!-- row 10 -->
<section class="slide banner-text">
  <div class="ph crew" role="img" aria-label="Construction team on site" style="left:0;top:0;width:356px;height:86px"></div>
  <div class="ico" style="left:78px;top:108px;width:18px;height:18px"></div>
  <h2 class="h" style="left:14px;top:130px;width:120px">Neque porro quisquam est qui dolorem ipsum quia dolor sit amet</h2>
  <p class="tx" style="left:170px;top:110px;width:170px">Ground up builds delivered on time and on budget.</p>
</section>

<section class="slide team">
  <h2 class="h big" style="left:0;width:356px;top:14px;text-align:center">Our Team</h2>
  <div class="diamond" style="left:64px;top:46px;width:44px;height:44px;border:1px solid var(--orange)"></div>
  <div class="ph crew diamond" role="img" aria-label="Portrait of team member" style="left:69px;top:51px;width:34px;height:34px"></div>
  <div class="diamond" style="left:156px;top:46px;width:44px;height:44px;border:1px solid var(--orange)"></div>
  <div class="ph warm diamond" role="img" aria-label="Portrait of team member" style="left:161px;top:51px;width:34px;height:34px"></div>
  <div class="diamond" style="left:248px;top:46px;width:44px;height:44px;border:1px solid var(--orange)"></div>
  <div class="ph crew diamond" role="img" aria-label="Portrait of team member" style="left:253px;top:51px;width:34px;height:34px"></div>
  <p class="label" style="left:56px;width:60px;top:108px;text-align:center">Lorem ipsum</p><p class="tx c" style="left:56px;width:60px;top:116px">Project director</p>
  <p class="label" style="left:148px;width:60px;top:108px;text-align:center">Lorem ipsum</p><p class="tx c" style="left:148px;width:60px;top:116px">Site manager</p>
  <p class="label" style="left:240px;width:60px;top:108px;text-align:center">Lorem ipsum</p><p class="tx c" style="left:240px;width:60px;top:116px">Estimating lead</p>
</section>

<section class="slide profile">
  <p class="tx" style="left:14px;top:34px;width:80px">Ground up builds delivered on time and on budget.</p>
  <div class="diamond" style="left:110px;top:30px;width:54px;height:54px;border:1px solid var(--orange)"></div>
  <div class="ph crew diamond" role="img" aria-label="Portrait of team member" style="left:116px;top:36px;width:42px;height:42px"></div>
  <p class="label" style="left:102px;width:70px;top:102px;text-align:center">Lorem ipsum</p>
  <div class="social" style="left:116px;top:118px"><span></span><span></span><span></span><span></span></div>
  <div style="left:210px;top:20px;width:130px;height:160px;border:1px solid var(--line)"></div>
  <p class="tx" style="left:220px;top:36px">Planning</p><div style="left:220px;top:44px;width:100px;height:4px;background:var(--orange)"></div>
  <p class="tx" style="left:220px;top:60px">Budget</p><div style="left:220px;top:68px;width:84px;height:4px;background:var(--orange)"></div>
  <p class="tx" style="left:220px;top:84px">Safety</p><div style="left:220px;top:92px;width:110px;height:4px;background:var(--orange)"></div>
  <p class="tx" style="left:220px;top:108px">Schedule</p><div style="left:220px;top:116px;width:74px;height:4px;background:var(--orange)"></div>
  <p class="tx" style="left:220px;top:132px">Quality</p><div style="left:220px;top:140px;width:96px;height:4px;background:var(--orange)"></div>
</section>

<!-- row 11 -->
<section class="slide process-wave">
  <h2 class="h" style="left:0;width:356px;top:14px;text-align:center">Lorem ipsum dolor sit amet, consectetur adipiscing elit</h2>
  <svg style="left:20px;top:60px" width="316" height="50" viewBox="0 0 316 50" aria-hidden="true">
    <path d="M0 25 C30 0 40 50 70 25 S110 0 140 25 S180 50 210 25 S250 0 280 25 S310 50 316 25" fill="none" stroke="#cf7424" stroke-width="1.5"/>
    <g fill="#fff" stroke="#cf7424" stroke-width="2"><circle cx="30" cy="25" r="16"/><circle cx="94" cy="25" r="16"/><circle cx="158" cy="25" r="16"/><circle cx="222" cy="25" r="16"/><circle cx="286" cy="25" r="16"/></g>
    <g fill="#cf7424"><rect x="26" y="21" width="8" height="8"/><rect x="90" y="21" width="8" height="8"/><rect x="154" y="21" width="8" height="8"/><rect x="218" y="21" width="8" height="8"/><rect x="282" y="21" width="8" height="8"/></g>
  </svg>
  <p class="tx c" style="left:30px;width:40px;top:118px">Site review</p>
  <p class="tx c" style="left:94px;width:40px;top:118px">Cost estimate</p>
  <p class="tx c" style="left:158px;width:40px;top:118px">Permit filing</p>
  <p class="tx c" style="left:222px;width:40px;top:118px">Shell build</p>
  <p class="tx c" style="left:286px;width:40px;top:118px">Handover</p>
</section>

<section class="slide bar-chart">
  <h2 class="h" style="left:150px;top:14px;width:194px;text-align:right">Neque porro quisquam est qui dolorem</h2>
  <svg style="left:30px;top:40px" width="280" height="140" viewBox="0 0 280 140" aria-hidden="true">
    <g fill="#cf7424">
      <rect x="10" y="110" width="14" height="30"/><rect x="34" y="80" width="14" height="60"/><rect x="58" y="60" width="14" height="80"/>
      <rect x="82" y="20" width="14" height="120"/><rect x="106" y="50" width="14" height="90"/><rect x="130" y="70" width="14" height="70"/>
      <rect x="154" y="88" width="14" height="52"/><rect x="178" y="64" width="14" height="76"/><rect x="202" y="62" width="14" height="78"/>
    </g>
    <g font-family="Montserrat, sans-serif" font-size="6" fill="#cf7424" text-anchor="middle">
      <text x="17" y="106">20</text><text x="41" y="76">40</text><text x="65" y="56">55</text><text x="89" y="16">85</text><text x="113" y="46">62</text><text x="137" y="66">48</text><text x="161" y="84">35</text><text x="185" y="60">52</text><text x="209" y="58">54</text>
    </g>
  </svg>
</section>

<section class="slide donuts">
  <h2 class="h" style="left:226px;top:20px;width:120px;text-align:right">1914 translation by H. Corwell</h2>
  <p class="tx" style="left:226px;top:44px;width:120px;text-align:right">Ground up builds delivered on time and on budget.</p>
  <svg style="left:20px;top:70px" width="220" height="80" viewBox="0 0 220 80" aria-hidden="true">
    <g fill="none" stroke-width="9">
      <circle cx="35" cy="30" r="24" stroke="#f3d2b3"/><circle cx="35" cy="30" r="24" stroke="#cf7424" stroke-dasharray="116 151" transform="rotate(-90 35 30)"/>
      <circle cx="110" cy="30" r="24" stroke="#f3d2b3"/><circle cx="110" cy="30" r="24" stroke="#cf7424" stroke-dasharray="104 151" transform="rotate(-90 110 30)"/>
      <circle cx="185" cy="30" r="24" stroke="#f3d2b3"/><circle cx="185" cy="30" r="24" stroke="#cf7424" stroke-dasharray="134 151" transform="rotate(-90 185 30)"/>
    </g>
    <g font-family="Montserrat, sans-serif" font-weight="700" font-size="9" fill="#cf7424" text-anchor="middle">
      <text x="35" y="76">77%</text><text x="110" y="76">69%</text><text x="185" y="76">89%</text>
    </g>
  </svg>
</section>

<!-- row 12 -->
<section class="slide world">
  <div class="map" role="img" aria-label="World map in amber" style="left:100px;top:10px;width:240px;height:140px"></div>
  <h2 class="h" style="left:14px;top:152px">Lorem ipsum<br>dolor sit</h2>
  <p class="tx" style="left:14px;top:174px;width:150px">Ground up builds delivered on time and on budget.</p>
</section>

<section class="slide national">
  <div class="map" role="img" aria-label="Map of the United States in amber" style="left:20px;top:12px;width:190px;height:120px"></div>
  <h2 class="h" style="left:190px;top:126px;width:156px;text-align:right">Section 1.10.33 of "de finibus bonorum et malorum", written by Aurelius Ventor in 45 BC</h2>
  <p class="tx" style="left:190px;top:170px;width:156px;text-align:right">White box shells ready for tenant fit out work.</p>
</section>

<section class="slide chain">
  <h2 class="h" style="left:0;width:356px;top:14px;text-align:center">Lorem ipsum dolor sit amet, consectetur adipiscing elit</h2>
  <div style="left:90px;top:84px;width:180px;height:5px;background:var(--orange)"></div>
  <div class="year" style="left:80px;top:76px;border-width:3px"></div>
  <div class="year" style="left:140px;top:76px;border-width:3px"></div>
  <div class="year" style="left:200px;top:76px;border-width:3px"></div>
  <div class="year" style="left:260px;top:76px;border-width:3px"></div>
  <p class="tx c" style="left:66px;width:48px;top:108px">Initial consult</p>
  <p class="tx c" style="left:126px;width:48px;top:108px">Design phase</p>
  <p class="tx c" style="left:186px;width:48px;top:108px">Build start</p>
  <p class="tx c" style="left:246px;width:48px;top:108px">Walkthrough</p>
</section>

<!-- row 13 -->
<section class="slide line-chart">
  <h2 class="h" style="left:14px;top:36px;width:90px">Neque porro quisquam est qui dolorem ipsum</h2>
  <p class="tx" style="left:14px;top:76px;width:90px">Ground up builds delivered on time and on budget.</p>
  <svg style="left:130px;top:40px" width="210" height="110" viewBox="0 0 210 110" aria-hidden="true">
    <line x1="0" y1="100" x2="210" y2="100" stroke="#dcdcdc"/>
    <polyline points="10,80 40,62 70,70 100,30 130,50 160,44 190,66" fill="none" stroke="#e7a56a" stroke-width="1.5"/>
    <g fill="#fff" stroke="#cf7424"><circle cx="10" cy="80" r="2.5"/><circle cx="40" cy="62" r="2.5"/><circle cx="70" cy="70" r="2.5"/><circle cx="100" cy="30" r="2.5"/><circle cx="130" cy="50" r="2.5"/><circle cx="160" cy="44" r="2.5"/><circle cx="190" cy="66" r="2.5"/></g>
  </svg>
</section>

<section class="slide contact">
  <div class="logo large" style="left:40px;top:78px">HARBOR</div>
  <h2 class="h" style="left:200px;top:66px;text-transform:none">Harbor Builders</h2>
  <p class="tx" style="left:200px;top:80px;width:130px">Commercial builders, Dallas TX<br>www.harborbgx.example</p>
  <div class="social" style="left:226px;top:120px"><span></span><span></span><span></span></div>
  <div class="ph plan" role="img" aria-label="Hard hat on plans" style="left:0;top:182px;width:356px;height:18px"></div>
</section>

<section class="slide location">
  <div class="logo large" style="left:20px;top:78px">HARBOR</div>
  <div class="social" style="left:30px;top:112px"><span></span><span></span><span></span></div>
  <div role="img" aria-label="Street map of the office area" style="left:178px;top:0;width:178px;height:200px;background:linear-gradient(135deg,#f1f2f3 0%,#dfe2e5 45%,#c9cdd1 100%)"></div>
  <svg style="left:248px;top:34px" width="12" height="18" viewBox="0 0 12 18" aria-hidden="true"><path d="M6 18 C6 18 0 10 0 6 A6 6 0 0 1 12 6 C12 10 6 18 6 18 Z" fill="#3b3b3b"/><circle cx="6" cy="6" r="2" fill="#fff"/></svg>
</section>

</main>
</body>
</html>
```